Bref créative
New stationary
stationary refresh
Professional
Gordon Pavlicek
418 Tamsin Ave.
Metairie, LA 70001
please leave room for individual cell phone #
gord@valcorix.net
www.valcorix.net
just main logo with black or light grey background. kinds modern

```html
<!DOCTYPE html>
<html lang="en">
<head>
<meta charset="utf-8">
<title>Valcorix Stationery</title>
<link href="https://fonts.googleapis.com/css2?family=Montserrat:wght@700;800&family=Open+Sans:wght@400;600&display=swap" rel="stylesheet">
<style>
  :root{
    --board:#3b3b3d;
    --board-dark:#2c2c2e;
    --paper:#ffffff;
    --red:#d71920;
    --ink:#1d1d1f;
    --grey:#9a9a9c;
    --faint:#f1eeee;
    --label:#8d8d90;
  }
  *{margin:0;padding:0;box-sizing:border-box}
  html,body{width:1200px;height:310px;overflow:hidden}
  body{background:radial-gradient(ellipse at 50% 40%,var(--board) 0%,var(--board-dark) 100%);font-family:"Open Sans",sans-serif;position:relative}
  .brand{display:flex;align-items:center;gap:4px;font-family:"Montserrat",sans-serif;font-weight:800;letter-spacing:-.02em;line-height:1;white-space:nowrap}
  .brand .mark{background:var(--red);flex:none}
  .brand .name{color:var(--ink)}
  .brand.on-dark .name{color:var(--paper)}
  .board-logo{position:absolute;left:20px;top:12px}
  .board-logo .mark{width:24px;height:24px}
  .board-logo .name{font-size:27px;color:var(--paper)}
  .board-logo .tagline{display:block;margin:4px 0 0 30px;font-size:6.5px;letter-spacing:.32em;color:var(--grey);font-family:"Montserrat",sans-serif;font-weight:700;white-space:nowrap}
  .item{position:absolute;background:var(--paper);overflow:hidden;box-shadow:0 2px 6px rgba(0,0,0,.45)}
  .label{position:absolute;font-size:5px;color:var(--label);text-align:center;white-space:nowrap}
  .wave{position:absolute;left:0;bottom:0;width:100%}
  .card{width:110px;height:60px}
  .card .brand{position:absolute;left:7px;top:7px}
  .card .brand .mark{width:8px;height:8px}
  .card .brand .name{font-size:10px}
  .card .details{position:absolute;left:7px;top:21px;font-size:4px;line-height:1.4;color:var(--ink);white-space:nowrap}
  .card .details strong{color:var(--red);font-size:4.6px}
  .card.dark{background:#1a1a1b}
  .card.dark .mark-lone{position:absolute;left:45px;top:20px;width:20px;height:20px;background:var(--red)}
  .card.dark .brand{left:28px;top:25px}
  .letterhead{width:200px;height:246px;top:22px}
  .letterhead .brand{position:absolute;left:14px;top:12px}
  .letterhead .brand .mark{width:11px;height:11px}
  .letterhead .brand .name{font-size:14px}
  .letterhead .contact{position:absolute;right:14px;top:12px;font-size:3.5px;line-height:1.45;color:var(--grey);white-space:nowrap}
  .letterhead .faint-mark{position:absolute;left:68px;top:90px;width:64px;height:64px;background:var(--faint)}
  .letterhead .footer{position:absolute;left:0;right:0;bottom:6px;font-size:3.5px;color:var(--paper);text-align:center}
  .envelope{width:222px;height:96px;left:700px}
  .envelope .brand{position:absolute;left:10px;top:10px}
  .envelope .brand .mark{width:9px;height:9px}
  .envelope .brand .name{font-size:11px}
  .envelope .address{position:absolute;left:10px;top:25px;font-size:3.5px;line-height:1.4;color:var(--grey);white-space:nowrap}
  .flat-env{position:absolute;left:950px;width:226px}
</style>
</head>
<body>

<div class="board-logo">
  <div class="brand on-dark"><span class="mark"></span><span class="name">valcorix</span></div>
  <span class="tagline">BUILT ON TRUST</span>
</div>

<!-- business cards, front -->
<div class="item card" style="left:18px;top:118px">
  <div class="brand"><span class="mark"></span><span class="name">valcorix</span></div>
  <div class="details"><strong>Gordon Pavlicek</strong><br>Sales Director<br>418 Tamsin Ave.<br>Metairie, LA 70001<br>gord@valcorix.net</div>
  <svg class="wave" viewBox="0 0 100 20" preserveAspectRatio="none" height="10"><path d="M0 5C30 16 60-2 100 3V7C60 1 30 20 0 9Z" fill="#1d1d1f"/><path d="M0 9C30 20 60 1 100 7V20H0Z" fill="#d71920"/></svg>
</div>
<div class="item card" style="left:138px;top:118px">
  <div class="brand"><span class="mark"></span><span class="name">valcorix</span></div>
  <div class="details"><strong>Gordon Pavlicek</strong><br>Cell 504 555 0142<br>Office 504 555 0100<br>gord@valcorix.net<br>www.valcorix.net</div>
  <svg class="wave" viewBox="0 0 100 20" preserveAspectRatio="none" height="10"><path d="M0 5C30 16 60-2 100 3V7C60 1 30 20 0 9Z" fill="#1d1d1f"/><path d="M0 9C30 20 60 1 100 7V20H0Z" fill="#d71920"/></svg>
</div>
<div class="label" style="left:18px;top:184px;width:230px">Business Card Front</div>

<!-- business cards, back -->
<div class="item card dark" style="left:18px;top:212px"><span class="mark-lone"></span></div>
<div class="item card dark" style="left:138px;top:212px">
  <div class="brand on-dark"><span class="mark"></span><span class="name">valcorix</span></div>
</div>
<div class="label" style="left:18px;top:278px;width:230px">Business Card Back</div>

<!-- letterheads -->
<div class="item letterhead" style="left:270px">
  <div class="brand"><span class="mark"></span><span class="name">valcorix</span></div>
  <div class="contact">418 Tamsin Ave.<br>Metairie, LA 70001<br>gord@valcorix.net<br>www.valcorix.net</div>
  <span class="faint-mark"></span>
  <svg class="wave" viewBox="0 0 100 20" preserveAspectRatio="none" height="40"><path d="M0 5C30 16 60-2 100 3V7C60 1 30 20 0 9Z" fill="#1d1d1f"/><path d="M0 9C30 20 60 1 100 7V20H0Z" fill="#d71920"/></svg>
  <div class="footer">www.valcorix.net</div>
</div>
<div class="label" style="left:270px;top:274px;width:200px">Letterhead Page One</div>

<div class="item letterhead" style="left:488px">
  <div class="brand"><span class="mark"></span><span class="name">valcorix</span></div>
  <span class="faint-mark"></span>
  <svg class="wave" viewBox="0 0 100 20" preserveAspectRatio="none" height="40"><path d="M0 5C30 16 60-2 100 3V7C60 1 30 20 0 9Z" fill="#1d1d1f"/><path d="M0 9C30 20 60 1 100 7V20H0Z" fill="#d71920"/></svg>
  <div class="footer">www.valcorix.net</div>
</div>
<div class="label" style="left:488px;top:274px;width:200px">Letterhead Page Two</div>

<!-- envelope fronts -->
<div class="item envelope" style="top:48px">
  <div class="brand"><span class="mark"></span><span class="name">valcorix</span></div>
  <div class="address">418 Tamsin Ave.<br>Metairie, LA 70001</div>
  <svg class="wave" viewBox="0 0 100 20" preserveAspectRatio="none" height="22"><path d="M0 5C30 16 60-2 100 3V7C60 1 30 20 0 9Z" fill="#1d1d1f"/><path d="M0 9C30 20 60 1 100 7V20H0Z" fill="#d71920"/></svg>
</div>
<div class="label" style="left:700px;top:150px;width:222px">Envelope Front</div>

<div class="item envelope" style="top:172px">
  <div class="brand"><span class="mark"></span><span class="name">valcorix</span></div>
  <div class="address">418 Tamsin Ave.<br>Metairie, LA 70001</div>
  <svg class="wave" viewBox="0 0 100 20" preserveAspectRatio="none" height="22"><path d="M0 5C30 16 60-2 100 3V7C60 1 30 20 0 9Z" fill="#1d1d1f"/><path d="M0 9C30 20 60 1 100 7V20H0Z" fill="#d71920"/></svg>
</div>

<!-- envelope backs -->
<svg class="flat-env" style="top:50px" height="58" viewBox="0 0 226 58">
  <rect width="226" height="58" fill="#ffffff"/>
  <path d="M0 0H226L113 36Z" fill="#1d1d1f"/>
  <rect x="106" y="16" width="14" height="14" fill="#d71920"/>
</svg>
<svg class="flat-env" style="top:116px" height="58" viewBox="0 0 226 58">
  <rect width="226" height="58" fill="#ffffff"/>
  <path d="M0 58L113 26L226 58" fill="none" stroke="#dcdcdc" stroke-width="1"/>
  <path d="M0 0H226L113 36Z" fill="#d71920"/>
  <rect x="108" y="18" width="10" height="10" fill="#ffffff"/>
</svg>
<svg class="flat-env" style="top:184px" height="58" viewBox="0 0 226 58">
  <rect width="226" height="58" fill="#ffffff"/>
  <path d="M0 0L113 36L226 0M0 58L113 26L226 58" fill="none" stroke="#d4d4d4" stroke-width="1"/>
</svg>
<div class="label" style="left:950px;top:248px;width:226px">Envelope Back</div>

</body>
</html>
```